Family Ranch with a hobby vineyard needs 2 wine labels for our first harvest

Design 2 wine labels (front and back) with the Brindor Ranch logo.
Label 1:
Sauvignon Blanc
Alc. 12.5% by Vol.
Palos Verdes Peninsula - add as the region
Year 2022
Label 2:
Cabernet Sauvignon
Alc. 13.5% by Vol.
Year 2022
For the back label design:
GOVERNMENT WARNING: (1) According to the Surgeon General, women
should not drink alcoholic beverages during pregnancy because of the risk of
birth defects. (2) Consumption of alcoholic beverages impairs your ability to
drive a car or operate machinery, and may cause health problems.
Contains Sulfates.
750ML
I just received the bottles and have attached a picture.
Look and feel
Each slider illustrates characteristics of the customer's brand and the style your logo design should communicate.

```html
<!DOCTYPE html>
<html lang="en">
<head>
<meta charset="utf-8">
<title>Brindor Ranch – Wine Labels 2022</title>
<link rel="stylesheet" href="https://fonts.googleapis.com/css2?family=Raleway:ital,wght@0,300;0,400;0,600;0,700;1,300&display=swap">
<style>
  :root {
    --canvas: #f4f4f4;
    --cabernet: #6a1f42;
    --blanc: #323c2b;
    --copper: #c47d46;
    --copper-light: #efc9a0;
    --copper-dark: #8e4a22;
    --vintage-band: #ececec;
    --vintage-ink: #3a1424;
    --label-ink: #ffffff;
    --label-ink-soft: rgba(255,255,255,0.86);
  }
  * { box-sizing: border-box; margin: 0; padding: 0; }
  html, body { width: 1200px; height: 1000px; overflow: hidden; }
  body {
    background: var(--canvas);
    font-family: "Raleway", sans-serif;
    color: var(--label-ink);
    position: relative;
  }

  /* ---------- front labels ---------- */
  .front-label {
    position: absolute;
    top: 324px;
    width: 254px;
    height: 352px;
    display: flex;
    flex-direction: column;
  }
  .front-label--cabernet { left: 310px; }
  .front-label--blanc { left: 628px; }

  .vintage-band {
    height: 38px;
    background: var(--vintage-band);
    display: flex;
    align-items: center;
    justify-content: center;
    font-weight: 700;
    font-size: 22px;
    letter-spacing: 16px;
    padding-left: 16px;
    color: var(--vintage-ink);
  }
  .front-label--blanc .vintage-band { color: #1f2a1c; }

  .copper-rule {
    background: linear-gradient(90deg, var(--copper-dark), var(--copper) 30%, var(--copper-light) 55%, var(--copper) 75%, var(--copper-dark));
  }
  .copper-rule--top { height: 11px; }
  .copper-rule--bottom { height: 14px; }

  .label-body {
    flex: 1;
    display: flex;
    flex-direction: column;
    align-items: center;
    text-align: center;
  }
  .front-label--cabernet .label-body { background: var(--cabernet); }
  .front-label--blanc .label-body { background: var(--blanc); }

  .brand-mark {
    display: flex;
    flex-direction: column;
    align-items: center;
    gap: 10px;
  }
  .brand-mark__dot {
    border-radius: 50%;
    background: var(--copper);
  }
  .brand-mark__name {
    font-weight: 600;
    color: var(--label-ink);
    text-transform: uppercase;
    line-height: 1;
  }
  .front-label .brand-mark { margin-top: 20px; }
  .front-label .brand-mark__dot { width: 58px; height: 58px; }
  .front-label .brand-mark__name { font-size: 23px; letter-spacing: 1px; width: 170px; line-height: 1.15; }

  .varietal-front {
    margin-top: 26px;
    font-weight: 700;
    font-size: 19px;
    letter-spacing: 3px;
    line-height: 23px;
    color: var(--copper);
    text-transform: uppercase;
  }
  .region {
    margin-top: 20px;
    font-style: italic;
    font-weight: 300;
    font-size: 14px;
    color: var(--label-ink);
  }
  .abv {
    margin-top: 22px;
    font-weight: 300;
    font-size: 14px;
    color: var(--label-ink);
  }

  /* ---------- back labels ---------- */
  .back-label {
    position: absolute;
    top: 372px;
    width: 233px;
    height: 286px;
    padding: 20px 26px 0;
    display: flex;
    flex-direction: column;
    align-items: center;
  }
  .back-label--cabernet { left: 19px; background: var(--cabernet); }
  .back-label--blanc { left: 942px; background: var(--blanc); }

  .back-label .brand-mark { gap: 6px; }
  .back-label .brand-mark__dot { width: 36px; height: 36px; background: var(--label-ink); }
  .back-label .brand-mark__name { font-size: 14px; letter-spacing: 0.5px; }

  .varietal-back {
    margin-top: 12px;
    font-weight: 700;
    font-size: 11.5px;
    letter-spacing: 2px;
    text-transform: uppercase;
  }
  .warning {
    margin-top: 10px;
    font-weight: 300;
    font-size: 8.4px;
    line-height: 10.7px;
    text-align: justify;
    color: var(--label-ink-soft);
  }
  .back-footer {
    width: 100%;
    margin-top: 10px;
    display: flex;
    flex-direction: column;
    gap: 6px;
  }
  .sulfites {
    font-size: 8.6px;
    font-weight: 300;
    color: var(--label-ink-soft);
  }
  .disposal-icons { display: flex; gap: 5px; }
  .disposal-icons span {
    width: 14px; height: 14px;
    border-radius: 50%;
    background: var(--label-ink);
  }
  .volume {
    font-size: 13.5px;
    font-weight: 400;
  }
</style>
</head>
<body>

  <!-- back label: cabernet -->
  <section class="back-label back-label--cabernet">
    <div class="brand-mark">
      <span class="brand-mark__dot"></span>
      <span class="brand-mark__name">Brindor Ranch</span>
    </div>
    <h2 class="varietal-back">Cabernet Sauvignon</h2>
    <p class="warning">GOVERNMENT WARNING: (1) According to the Surgeon General, women should not drink alcoholic beverages during pregnancy because of the risk of birth defects. (2) Consumption of alcoholic beverages impairs your ability to drive a car or operate machinery, and may cause health problems.</p>
    <div class="back-footer">
      <p class="sulfites">Contains Sulfates.</p>
      <div class="disposal-icons"><span></span><span></span><span></span></div>
      <p class="volume">750 ML</p>
    </div>
  </section>

  <!-- front label: cabernet -->
  <section class="front-label front-label--cabernet">
    <div class="vintage-band">2022</div>
    <div class="copper-rule copper-rule--top"></div>
    <div class="label-body">
      <div class="brand-mark">
        <span class="brand-mark__dot"></span>
        <span class="brand-mark__name">Brindor Ranch</span>
      </div>
      <h1 class="varietal-front">Cabernet<br>Sauvignon</h1>
      <p class="region">Palos Verdes Peninsula</p>
      <p class="abv">Alc. 13,5% Vol.</p>
    </div>
    <div class="copper-rule copper-rule--bottom"></div>
  </section>

  <!-- front label: sauvignon blanc -->
  <section class="front-label front-label--blanc">
    <div class="vintage-band">2022</div>
    <div class="copper-rule copper-rule--top"></div>
    <div class="label-body">
      <div class="brand-mark">
        <span class="brand-mark__dot"></span>
        <span class="brand-mark__name">Brindor Ranch</span>
      </div>
      <h1 class="varietal-front">Sauvignon<br>Blanc</h1>
      <p class="region">Palos Verdes Peninsula</p>
      <p class="abv">Alc. 12,5% Vol.</p>
    </div>
    <div class="copper-rule copper-rule--bottom"></div>
  </section>

  <!-- back label: sauvignon blanc -->
  <section class="back-label back-label--blanc">
    <div class="brand-mark">
      <span class="brand-mark__dot"></span>
      <span class="brand-mark__name">Brindor Ranch</span>
    </div>
    <h2 class="varietal-back">Sauvignon Blanc</h2>
    <p class="warning">GOVERNMENT WARNING: (1) According to the Surgeon General, women should not drink alcoholic beverages during pregnancy because of the risk of birth defects. (2) Consumption of alcoholic beverages impairs your ability to drive a car or operate machinery, and may cause health problems.</p>
    <div class="back-footer">
      <p class="sulfites">Contains Sulfates.</p>
      <div class="disposal-icons"><span></span><span></span><span></span></div>
      <p class="volume">750 ML</p>
    </div>
  </section>

</body>
</html>
```